Ribbon Cutting Ceremony Invitation for Solar Company

Need 8.5 x 11 Ribbon Cutting Invitation Design to be used for digital and print. The design should be professional yet creative. It should showcase the theme of a ribbon cutting with some sort of style resembling solar energy. There could also be an option to include a placeholder for a photo of the facility, but that is up to your creative direction. Thanks designers!

Words that should be on it are below:

RIBBON CUTTING CEREMONY

WE FORMALLY INVITE YOU TO THE RIBBON CUTTING EVENT FOR THE NEW SOLAR SYSTEM @ SEABRAMBLE HOTEL AND RESORT.

DATE AND TIME

Use this logo in one of the corners: https://files.plenvarq-media.net/assets/k/kd/Vexa_Energy.png - Let me know if you need it in a different version, transparent, or all white.

PLEASE ASK ME ANY QUESTIONS!!!

Target Market(s)

Business Owners and Executives

Colors

Designer to choose colors to be used in the design.

Requirements
Must have
• Professional design with ribbon cutting and solar theme.

```html
<!DOCTYPE html>
<html lang="en">
<head>
<meta charset="utf-8">
<title>Ribbon Cutting Ceremony Invitation</title>
<link rel="stylesheet" href="https://fonts.googleapis.com/css2?family=Playfair+Display:wght@400&family=Arimo:wght@400;600&display=swap">
<style>
  :root {
    --backdrop: #e9e7e3;
    --paper: #ffffff;
    --charcoal: #3a3a3c;
    --charcoal-deep: #2c2c2e;
    --gold-light: #f3d873;
    --gold: #d4a92c;
    --gold-deep: #a67c12;
    --title-ink: #5a4714;
    --soft-white: #d8d8d8;
  }
  * { box-sizing: border-box; margin: 0; padding: 0; }
  html, body {
    width: 1200px;
    height: 849px;
    overflow: hidden;
    background: var(--backdrop);
  }
  .invitation {
    position: absolute;
    left: 291px;
    top: 24px;
    width: 618px;
    height: 800px;
    background: var(--paper);
    box-shadow: 0 6px 24px rgba(0,0,0,0.18);
  }
  .invitation__shapes {
    position: absolute;
    inset: 0;
  }
  .invitation__title {
    position: absolute;
    left: 28px;
    top: 30px;
    font-family: "Playfair Display", serif;
    font-weight: 400;
    font-size: 38px;
    line-height: 42px;
    letter-spacing: 1px;
    color: var(--title-ink);
  }
  .ribbon-art {
    position: absolute;
    left: 150px;
    top: 360px;
    width: 200px;
    height: 170px;
    background: linear-gradient(135deg, var(--gold-light) 0%, var(--gold) 45%, var(--charcoal) 100%);
  }
  .brand {
    position: absolute;
    left: 372px;
    top: 428px;
    font-family: "Arimo", sans-serif;
    font-weight: 600;
    font-size: 28px;
    line-height: 34px;
    color: var(--paper);
    white-space: nowrap;
  }
  .invite-copy {
    position: absolute;
    left: 60px;
    top: 612px;
    width: 440px;
    font-family: "Arimo", sans-serif;
    text-transform: uppercase;
    font-size: 13px;
    line-height: 18px;
    color: var(--gold);
  }
  .event-time {
    position: absolute;
    left: 90px;
    top: 678px;
    font-family: "Arimo", sans-serif;
    font-size: 12px;
    line-height: 16px;
    color: var(--soft-white);
  }
</style>
</head>
<body>
  <article class="invitation">
    <svg class="invitation__shapes" width="618" height="800" viewBox="0 0 618 800" aria-hidden="true">
      <defs>
        <linearGradient id="gold-foil" x1="0" y1="0" x2="1" y2="1">
          <stop offset="0" stop-color="#b8891a"/>
          <stop offset="0.45" stop-color="#f3d873"/>
          <stop offset="1" stop-color="#c99a24"/>
        </linearGradient>
        <linearGradient id="charcoal-fade" x1="0" y1="0" x2="0" y2="1">
          <stop offset="0" stop-color="#3f3f41"/>
          <stop offset="1" stop-color="#2c2c2e"/>
        </linearGradient>
      </defs>
      <polygon class="dark-panel" points="470,18 600,18 600,782 18,782 18,500" fill="url(#charcoal-fade)"/>
      <polygon class="gold-corner" points="0,0 420,0 0,460" fill="url(#gold-foil)"/>
    </svg>

    <h1 class="invitation__title">RIBBON<br>CUTTING<br>CEREMONY</h1>

    <div class="ribbon-art" role="img" aria-label="Illustration of a gold ribbon being cut with gold scissors"></div>
    <div class="brand">Vexa Energy</div>

    <p class="invite-copy">We formally invite you to the ribbon cutting event for the new solar system @ Seabramble Hotel and Resort.</p>
    <p class="event-time">6th January 2020, 10:00 pm onwards.</p>
  </article>
</body>
</html>
```